Revamp a website that sells books on machine learning and A.I

Hello I would like to create a minimalist concept to revamp this website:

www.quillvane.co.uk

We can change everything including the logo.

Somethings that I don't like:
- Generic images of people.
- Robot images.

The books are about the mathematics for machine learning and A.I and I would like for the website to have a blog as well as a scheduling tool, were people can book a call with me.

The scheduling tool, needs to have text and different tiers, for example 15 m free and 60 m 45 usd

Target Market(s)

university students and mathematics enthusiasts

Industry/Entity Type

machine learning, education, books, mathematics, A.I

Number of Pages Required

4 page

Requirements
Must have
• Landing Page, blog page, scheduling page, optimised conversion funnel
Should not have
• Arbitrary images from people or robots

```html
<!DOCTYPE html>
<html lang="en">
<head>
<meta charset="utf-8">
<title>Quillvane – Beneath the Model</title>
<link href="https://fonts.googleapis.com/css2?family=Barlow:wght@400;500;600;700&family=Poppins:wght@400;500;600&display=swap" rel="stylesheet">
<style>
:root{
  --orange:#f07b2a;
  --orange-deep:#ea5a16;
  --orange-light:#f5a55f;
  --ink:#1d1d1d;
  --text:#444;
  --muted:#666;
  --grey-band:#f2f2f2;
  --soft:#f6f6f6;
  --line:#d9d9d9;
  --white:#fff;
}
*{box-sizing:border-box;margin:0;padding:0}
html,body{width:1200px;height:3296px;overflow:hidden}
body{font-family:"Barlow",sans-serif;color:var(--text);background:var(--white);position:relative}
.abs{position:absolute}
.eyebrow{font-size:13px;font-weight:600;color:var(--orange);letter-spacing:.2px;text-transform:uppercase}
.section-title{font-size:30px;font-weight:700;color:var(--ink);text-transform:uppercase}
.center{left:0;width:1200px;text-align:center}

/* header */
.site-header{top:0;left:0;width:1200px;height:80px;background:var(--white)}
.brand{left:143px;top:24px;font-size:24px;font-weight:700;color:var(--ink);letter-spacing:.3px}
.nav a{position:absolute;top:34px;font-size:13px;font-weight:600;color:var(--ink);text-decoration:none}
.nav .active{color:var(--orange)}
.nav .active::before{content:"";position:absolute;left:-3px;right:-3px;top:-17px;height:4px;background:var(--orange)}
.account{top:33px;font-size:13px;color:var(--muted)}
.badge{left:1040px;top:26px;width:15px;height:15px;border-radius:50%;background:var(--orange);color:#fff;font-size:10px;text-align:center;line-height:15px}

/* hero */
.hero-panel{left:0;top:80px;width:600px;height:560px;background:linear-gradient(160deg,var(--orange-light),var(--orange-deep) 70%)}
.book-cover{border-radius:2px;box-shadow:6px 6px 14px rgba(0,0,0,.25)}
.hero-cover{left:145px;top:151px;width:316px;height:514px;background:linear-gradient(180deg,#f5c25a,#efb640)}
.hero-copy{left:650px;width:398px}
.hero-title{top:195px;font-size:32px;line-height:37px;font-weight:700;color:var(--ink)}
.hero-lead{top:273px;font-size:14px;line-height:20px;text-align:justify}
.hero-hook{top:403px;font-size:15.5px;line-height:20px;font-weight:600;color:var(--ink);text-align:justify}
.author-link{left:654px;top:480px;font-size:16px;font-weight:600;color:var(--orange)}
.btn{display:block;background:var(--orange);color:#fff;font-weight:700;text-align:center;text-transform:uppercase}
.hero-btn{left:656px;top:517px;width:158px;height:46px;line-height:46px;font-size:15px}

/* about */
.about-band{left:0;top:640px;width:1200px;height:238px;background:var(--grey-band)}
.about-name{left:143px;top:737px;font-family:"Poppins",sans-serif;font-size:27px;font-weight:600;color:var(--ink)}
.about-sub{left:145px;top:774px;font-size:13px}
.social-dot{left:148px;top:805px;width:12px;height:12px;background:var(--orange);border-radius:2px}
.about-text{left:466px;top:714px;width:592px;font-size:13.4px;line-height:22.5px}

/* books */
.book-card{border:3px solid var(--line);background:var(--white)}
.card-label{border:3px solid var(--line);background:var(--white);text-align:center;padding-top:18px;font-size:13.5px;font-weight:600;line-height:22px;color:var(--ink);text-transform:uppercase}
.card-label .price{display:block;font-size:18px;font-weight:700;color:var(--orange);margin-top:4px}
.card-label.is-hover{background:var(--orange);border-color:#f4b98c;color:#fff}
.card-label.is-hover .price{color:#fff}
.dl{width:32px;height:32px;border-radius:50%;border:1.5px solid #ddd;background:#fff}
.cart-btn{left:321px;top:1186px;width:142px;height:43px;line-height:43px;background:#000;color:#fff;font-size:15px;font-weight:700;text-align:center}

/* reviews */
.reviews{left:0;top:1533px;width:1200px;height:534px;background:radial-gradient(ellipse at 20% 120%,#e0661c,transparent 60%),linear-gradient(180deg,#ef7526,#ec7020)}
.review-text{left:289px;top:1802px;width:622px;text-align:center;color:#fff;font-size:17px;line-height:36px}
.review-rule{left:289px;top:1929px;width:621px;height:3px;background:#fff}
.arrow{width:52px;height:52px;border-radius:50%;background:#e66d1d}

/* blog */
.blog{left:0;top:2067px;width:1200px;height:704px;background:var(--soft)}
.post-card{background:#fff;box-shadow:0 2px 12px rgba(0,0,0,.08);font-family:"Poppins",sans-serif;padding:18px 24px}
.post-card h3{font-size:17px;font-weight:400;color:var(--ink);margin-bottom:10px}
.post-card p{font-size:12px;line-height:20px;color:var(--muted)}
.post-card .by{font-size:12px;color:var(--muted);text-decoration:underline;margin-top:8px;display:block}

/* footer */
.footer-title{font-family:"Poppins",sans-serif;font-size:27px;font-weight:600;color:var(--ink);text-transform:uppercase}
.quick a{position:absolute;left:176px;font-size:19px;color:var(--ink);text-decoration:none}
.chev{left:143px;font-size:18px;color:var(--orange)}
.call-box{left:143px;top:3075px;width:273px;height:94px;background:var(--grey-band)}
.field{border:1px solid #c8c8c8;background:var(--soft);font-size:13px;color:var(--ink);padding-left:22px;line-height:48px}
.tier{border:1px solid #c8c8c8;background:var(--soft);font-size:13px;color:var(--ink);line-height:48px;padding:0 18px}
.tier b{float:right;color:var(--orange);font-weight:600}
.submit{left:521px;top:3124px;width:124px;height:45px;line-height:45px;font-size:13px}
.copy{top:3241px;font-size:15px;color:var(--text)}
</style>
</head>
<body>

<header class="abs site-header">
  <div class="abs brand">QUILLVANE</div>
  <nav class="nav">
    <a class="active" style="left:522px">HOME</a>
    <a style="left:587px">ABOUT</a>
    <a style="left:661px">BOOKS</a>
    <a style="left:734px">CONTACT</a>
  </nav>
  <svg class="abs" style="left:906px;top:35px" width="13" height="13" viewBox="0 0 12 12"><circle cx="6" cy="3.5" r="3" fill="#333"/><path d="M0 12c0-4 3-5.5 6-5.5s6 1.5 6 5.5z" fill="#333"/></svg>
  <div class="abs account" style="left:926px">Login</div>
  <svg class="abs" style="left:997px;top:35px" width="14" height="13" viewBox="0 0 14 13"><path d="M0 1h3l2 7h7l2-5H4" fill="none" stroke="#333" stroke-width="1.8"/><circle cx="6" cy="11" r="1.4" fill="#333"/><circle cx="11" cy="11" r="1.4" fill="#333"/></svg>
  <div class="abs account" style="left:1019px">Cart</div>
  <div class="abs badge">0</div>
</header>

<section>
  <div class="abs hero-panel" role="img" aria-label="Orange gradient backdrop with a faint network of connected points"></div>
  <div class="abs book-cover hero-cover" role="img" aria-label="Cover of Beneath the Model volume 2, Calculus, illustrated with bees and a small machine"></div>
  <div class="abs eyebrow" style="left:653px;top:169px">Latest Release</div>
  <h1 class="abs hero-copy hero-title">BENEATH THE MODEL<br>VOL 2 – CALCULUS</h1>
  <p class="abs hero-copy hero-lead">Calculus is essential in machine learning and algorithm optimization, offering tools for function analysis and model tuning. Key concepts like derivatives and integrals are crucial for optimizing neural networks and minimizing error rates, making a strong understanding of calculus vital for success in these advanced fields.</p>
  <p class="abs hero-copy hero-hook" style="left:653px">Embark on a buzzing exploration of calculus in machine learning, where bees are your companions in deciphering the secrets of AI.</p>
  <div class="abs author-link">Tomas Reyland</div>
  <a class="abs btn hero-btn">Start Reading</a>
</section>

<section>
  <div class="abs about-band"></div>
  <div class="abs eyebrow" style="left:145px;top:712px">About Me</div>
  <h2 class="abs about-name">TOMAS REYLAND</h2>
  <div class="abs about-sub">A Mathematician and now a book writer</div>
  <div class="abs social-dot"></div>
  <p class="abs about-text">I am a mathematician with over a decade of experience in developing and deploying machine learning systems. My books are written in an conversational style with humour. They are rich in practical applications, enabling readers to not only grasp the concepts but also understand their real-world applications in the field of Data Science.</p>
</section>

<section>
  <div class="abs eyebrow center" style="top:944px">Our Books</div>
  <h2 class="abs section-title center" style="top:968px">There are two of them!</h2>

  <div class="abs book-card" style="left:214px;top:1024px;width:356px;height:367px"></div>
  <div class="abs book-cover" style="left:316px;top:1072px;width:145px;height:236px;background:linear-gradient(180deg,#f5c25a,#efb640)" role="img" aria-label="Cover of volume 2, Calculus"></div>
  <div class="abs cart-btn">ADD TO CART</div>
  <svg class="abs dl" style="left:514px;top:1046px" viewBox="0 0 32 32"><path d="M16 9v11M11 15l5 5 5-5M10 23h12" fill="none" stroke="#f07b2a" stroke-width="1.6"/></svg>
  <div class="abs card-label is-hover" style="left:247px;top:1331px;width:288px;height:109px">Beneath the Model Vol 2 -<br>Calculus Ebook PDF<span class="price">7,50 €</span></div>

  <div class="abs book-card" style="left:630px;top:1024px;width:356px;height:367px"></div>
  <div class="abs book-cover" style="left:735px;top:1072px;width:146px;height:236px;background:linear-gradient(180deg,#f7c15b,#eeb23f)" role="img" aria-label="Cover of volume 1, Linear Algebra"></div>
  <svg class="abs dl" style="left:930px;top:1046px" viewBox="0 0 32 32"><path d="M16 9v11M11 15l5 5 5-5M10 23h12" fill="none" stroke="#f07b2a" stroke-width="1.6"/></svg>
  <div class="abs card-label" style="left:663px;top:1331px;width:289px;height:109px">Beneath the Model Vol 1 -<br>Linear Algebra Ebook PDF<span class="price">7,50 €</span></div>
</section>

<section>
  <div class="abs reviews"></div>
  <div class="abs eyebrow center" style="top:1608px;color:#fff">Reviews</div>
  <h2 class="abs section-title center" style="top:1632px;color:#fff">Customer's Reviews</h2>
  <div class="abs center" style="top:1688px;font-size:90px;font-weight:700;color:#fff;line-height:90px;font-family:Georgia,serif">“</div>
  <div class="abs center" style="top:1772px;font-size:20px;color:#fff;letter-spacing:4px">★★★★★</div>
  <p class="abs review-text">"As a student going into ML without much of a linear algebra foundation, I'm finding this book highly useful. Starts form the basics and works at a reasonable pace to establish core ML concepts..."</p>
  <div class="abs review-rule"></div>
  <div class="abs center" style="top:1945px;font-size:25px;font-weight:700;color:#fff;padding-left:22px">Elin</div>
  <svg class="abs arrow" style="left:144px;top:1848px" viewBox="0 0 52 52"><path d="M29 20l-6 6 6 6" fill="none" stroke="#fff" stroke-width="2"/></svg>
  <svg class="abs arrow" style="left:1003px;top:1848px" viewBox="0 0 52 52"><path d="M23 20l6 6-6 6" fill="none" stroke="#fff" stroke-width="2"/></svg>
</section>

<section>
  <div class="abs blog"></div>
  <div class="abs eyebrow center" style="top:2140px">Blog Posts</div>
  <h2 class="abs section-title center" style="top:2163px">Latest Blog</h2>

  <div class="abs" style="left:143px;top:2229px;width:427px;height:346px;background:linear-gradient(160deg,#1c2230,#0c0f16)" role="img" aria-label="Dark photo of a laptop with glowing AI interface panels"></div>
  <div class="abs post-card" style="left:166px;top:2532px;width:382px;height:137px">
    <h3>Lorem ipsum dolor sit amet</h3>
    <p>Lorem ipsum dolor sit amet, consectetur adipiscing elit, sed do eiusmod tempor incididunt ut labore</p>
    <span class="by">By John Doe</span>
  </div>

  <div class="abs" style="left:600px;top:2229px;width:278px;height:203px;background:linear-gradient(135deg,#0b4f8a,#06182e)" role="img" aria-label="Blue-lit photo of hands typing on a laptop"></div>
  <div class="abs post-card" style="left:768px;top:2263px;width:288px;height:136px">
    <h3>Lorem ipsum dolor sit amet</h3>
    <p>Lorem ipsum dolor sit amet, cons ectetur adipiscing elit, sed do eiusmod</p>
    <span class="by">By John Doe</span>
  </div>

  <div class="abs" style="left:600px;top:2466px;width:278px;height:203px;background:linear-gradient(135deg,#0a3b73,#0a1a3a)" role="img" aria-label="Blue circuit board image with an AI chip"></div>
  <div class="abs post-card" style="left:768px;top:2500px;width:288px;height:136px">
    <h3>Lorem ipsum dolor sit amet</h3>
    <p>Lorem ipsum dolor sit amet, cons ectetur adipiscing elit, sed do eiusmod</p>
    <span class="by">By John Doe</span>
  </div>
</section>

<footer>
  <h2 class="abs footer-title" style="left:143px;top:2838px">Quick Links</h2>
  <div class="quick">
    <span class="abs chev" style="top:2900px">»</span><a style="top:2898px">Home</a>
    <span class="abs chev" style="top:2940px">»</span><a style="top:2938px">About</a>
    <span class="abs chev" style="top:2980px">»</span><a style="top:2978px">Books</a>
    <span class="abs chev" style="top:3020px">»</span><a style="top:3018px">Contact</a>
  </div>
  <div class="abs call-box">
    <svg class="abs" style="left:38px;top:32px" width="28" height="28" viewBox="0 0 24 24"><path d="M6.6 10.8a15 15 0 0 0 6.6 6.6l2.2-2.2c.3-.3.7-.4 1-.2 1.1.4 2.3.6 3.6.6.6 0 1 .4 1 1V20c0 .6-.4 1-1 1A17 17 0 0 1 3 4c0-.6.4-1 1-1h3.5c.6 0 1 .4 1 1 0 1.3.2 2.5.6 3.6.1.3 0 .7-.2 1z" fill="#f07b2a"/></svg>
    <div class="abs" style="left:82px;top:22px;font-size:14px;color:var(--ink)">Call Us Today :</div>
    <div class="abs" style="left:82px;top:45px;font-size:18px;font-weight:700;color:var(--ink)">+1 555 014 2276</div>
  </div>

  <h2 class="abs footer-title" style="left:517px;top:2837px">Book a call with me</h2>
  <div class="abs field" style="left:520px;top:2890px;width:258px;height:50px">First name</div>
  <div class="abs field" style="left:797px;top:2890px;width:259px;height:50px">Last name</div>
  <div class="abs field" style="left:520px;top:2961px;width:258px;height:50px">Email</div>
  <div class="abs field" style="left:797px;top:2961px;width:259px;height:50px">Phone</div>
  <div class="abs" style="left:521px;top:3032px;font-size:13px;font-weight:600;color:var(--ink)">Time</div>
  <div class="abs tier" style="left:520px;top:3058px;width:258px;height:50px"><span style="color:var(--orange)">☑</span> 15 mins<b>Free</b></div>
  <div class="abs tier" style="left:797px;top:3058px;width:259px;height:50px">☐ 60 mins<b>45 usd</b></div>
  <a class="abs btn submit">Submit</a>

  <div class="abs" style="left:143px;top:3210px;width:913px;height:1px;background:var(--line)"></div>
  <div class="abs copy center">© &nbsp;Copyrights 2024 | All Rights Reserved</div>
</footer>

</body>
</html>
```